Homepage layout for online ad network

Attached is our Calvrex Media logo and updated brief (I can't seem to delete the old logo and brief, but they're no longer relevant).

This project was originally posted with a different logo and corporate name, but we have decided to stay with our current logo and name and redesign the site.

Your design is for a homepage only - design, no coding (I'll get someone else to take your PSD and code it).

Your homepage will make use of a Flash slider - BUT YOU ARE NOT REQUIRED TO PROVIDE THE FLASH. Instead, simply provide the layout and at least two static examples out of the four different sections that will eventually be in the slider.

Much of this design is based on the design of a competitor (listed in the brief).

Please ask whatever questions you need to in order to clarify instructions.
Updates

Project updated to include new logo (and correspondingly new color scheme).

Brief changed slightly.

Thank you for submitting designs for this project in the past.

After some internal strategy work, we have decided to retain our initial corporate identity, Calvrex Media.

If you have submitted a design for the original brief and are available, please re-work your best prior design to reflect the color scheme in the newly uploaded logo.

Target Market(s)

This site is aimed primarily at young professionals who buy digital media on behalf of large advertisers.

Industry/Entity Type

Media

Requirements
Must have
• modern white space
Should not have
• no Flash outside of slider

```html
<!DOCTYPE html>
<html lang="en">
<head>
<meta charset="utf-8">
<title>Calvrex Media</title>
<link href="https://fonts.googleapis.com/css2?family=Arimo:wght@400;700&display=swap" rel="stylesheet">
<style>
  :root{
    --red:#c8202c;
    --red-deep:#a51f2c;
    --red-band:#b3262f;
    --red-active:#9c1d28;
    --ink:#1a1a1a;
    --ink-soft:#444;
    --grey-line:#cfcfcf;
    --page:#ffffff;
  }
  *{margin:0;padding:0;box-sizing:border-box}
  html,body{width:1200px;height:886px;overflow:hidden}
  body{position:relative;background:linear-gradient(#f6f6f6 0,#fff 60px,#fff 100%);font-family:"Arimo",Arial,sans-serif;color:var(--ink)}

  .brand{position:absolute;left:70px;top:52px;display:flex;align-items:center;gap:12px}
  .brand-mark{width:34px;height:34px;background:var(--red)}
  .brand-name{color:var(--red);font-size:30px;font-weight:400;line-height:34px}
  .brand-tagline{position:absolute;left:71px;top:98px;color:var(--ink-soft);font-size:13px}

  .main-nav{position:absolute;top:93px;right:70px;display:flex;font-size:15.5px}
  .main-nav a{color:var(--ink);text-decoration:none}
  .main-nav a.current{color:var(--red)}
  .main-nav .sep{margin:0 14px}

  .hero{position:absolute;left:71px;top:144px;width:1062px;height:288px;background:linear-gradient(180deg,#f3f3f3,#fff 35%,#f7f7f7);box-shadow:0 0 14px rgba(0,0,0,.22)}
  .hero-title{position:absolute;left:37px;top:60px;color:var(--red);font-size:25px;font-weight:700;letter-spacing:8px}
  .hero-text{position:absolute;left:37px;top:97px;width:420px;font-size:17.6px;line-height:21.6px;color:var(--ink)}
  .btn-more{position:absolute;left:37px;top:213px;width:100px;height:28px;border-radius:4px;background:linear-gradient(#e0222d,#a3101a);color:#fff;font-size:14.5px;font-weight:700;text-align:center;line-height:28px;box-shadow:0 2px 3px rgba(0,0,0,.35)}
  .hero-photo{position:absolute;left:690px;top:28px;width:265px;height:260px;border-radius:120px 120px 0 0;background:linear-gradient(160deg,#d9c6b0,#c8d79a 55%,#9cbf5a)}

  .tabs{position:absolute;left:71px;top:432px;width:1062px;height:93px;display:flex;background:var(--red-band)}
  .tab{position:relative;padding:16px 18px 0 18px;color:#fff;border-right:2px solid #8f1a24}
  .tab:last-child{border-right:none}
  .tab.active{background:var(--red-active)}
  .tab.active::before{content:"";position:absolute;left:128px;top:0;border:8px solid transparent;border-top-color:#fff;border-bottom:none}
  .tab h3{font-size:15.5px;font-weight:700;margin-bottom:5px}
  .tab p{font-size:15.5px;line-height:19px;text-align:justify}
  .tab:nth-child(1){width:267px}
  .tab:nth-child(2){width:269px}
  .tab:nth-child(3){width:265px}
  .tab:nth-child(4){width:261px}

  .insights{position:absolute;left:71px;top:546px;width:567px;height:233px;background:linear-gradient(#f1f1f1,#fff 30%,#f6f6f6);border-radius:4px;box-shadow:0 0 5px rgba(0,0,0,.12)}
  .insights h2{position:absolute;left:18px;top:14px;color:var(--red-deep);font-size:20px;font-weight:700}
  .insights .lead{position:absolute;left:18px;top:37px;font-size:16px;color:var(--ink)}
  .thumb{position:absolute;top:64px;width:154px;height:105px;border:1px solid var(--grey-line);background:#fff;padding:10px}
  .thumb .art{width:100%;height:100%}
  .thumb:nth-of-type(1){left:18px}
  .thumb:nth-of-type(2){left:190px}
  .thumb:nth-of-type(3){left:367px}
  .caption{position:absolute;top:185px;width:154px;text-align:center;font-size:14.5px;line-height:18px;color:var(--ink-soft)}

  .news{position:absolute;left:650px;top:546px;width:484px;height:233px;background:linear-gradient(#ececec,#e6e6e6)}
  .news-head{height:32px;background:var(--red);color:#fff;font-size:15px;font-weight:700;line-height:32px;padding-left:16px}
  .news-list{list-style:none;padding:19px 0 0 16px}
  .news-list li{margin-bottom:17px;font-size:15px;line-height:17px}
  .news-list strong{display:block;color:#2b2b2b}

  .site-footer{position:absolute;left:0;top:802px;width:1200px;height:84px;border-top:2px solid #cdcdcd;background:linear-gradient(#f4f4f4,#d9d9d9)}
  .footer-links{position:absolute;left:70px;top:15px;font-size:15.5px}
  .footer-links a{color:#000;text-decoration:none}
  .footer-links .sep{margin:0 7px}
  .social{position:absolute;top:13px;height:25px;border-radius:2px;font-size:12.5px;font-weight:700;line-height:25px;text-align:center;display:flex;align-items:center;justify-content:center;gap:6px}
  .social .dot{width:11px;height:11px}
  .social.chirp{left:950px;width:87px;background:linear-gradient(#d2f0fb,#8ed2ee);border:1px solid #7cc2df;color:#2a6f8f}
  .social.chirp .dot{background:#2a9fd0}
  .social.wall{left:1044px;width:89px;background:linear-gradient(#6e86bb,#3c5898);border:1px solid #2f4780;color:#fff}
  .social.wall .dot{background:#fff}
</style>
</head>
<body>
  <header>
    <div class="brand">
      <div class="brand-mark"></div>
      <div class="brand-name">Calvrex Media</div>
    </div>
    <div class="brand-tagline">audiences that move your brand</div>
    <nav class="main-nav">
      <a class="current" href="#">Beauty</a><span class="sep">|</span>
      <a href="#">Cooking</a><span class="sep">|</span>
      <a href="#">Parenting</a><span class="sep">|</span>
      <a href="#">Video</a>
    </nav>
  </header>

  <section class="hero">
    <h1 class="hero-title">COOKING</h1>
    <p class="hero-text">Lorem ipsum dolor sit amet, consectetur adipiscing elit. In mi libero, mollis eu consectetur ut, ultrices nec ipsum. Ut commodo, arcu eget aliquet vestibulum, turpis quam hendrerit sapien, in placerat lacus lacus vitae orci.</p>
    <div class="btn-more">Read More</div>
    <div class="hero-photo" role="img" aria-label="Photo of a smiling young family of three"></div>
  </section>

  <div class="tabs">
    <div class="tab"><h3>BEAUTY</h3><p>Lorem ipsum dolor siteit amet, conesd sectetur adipiscing elit.</p></div>
    <div class="tab active"><h3>COOKING</h3><p>Lorem ipsum dolor siteit amet, conesd sectetur adipiscing elit.</p></div>
    <div class="tab"><h3>PARENTING</h3><p>Lorem ipsum dolor siteit amet, conesd sectetur adipiscing elit.</p></div>
    <div class="tab"><h3>VIDEO</h3><p>Lorem ipsum dolor siteit amet, conesd sectetur adipiscing elit.</p></div>
  </div>

  <section class="insights">
    <h2>Calvrex Insights</h2>
    <p class="lead">Advanced audience analytics and actionable insights for marketers</p>
    <div class="thumb"><div class="art" role="img" aria-label="Folded newspaper with an extra edition headline" style="background:linear-gradient(135deg,#f2f2f2,#c9c9c9 60%,#8a8a8a)"></div></div>
    <div class="thumb"><div class="art" role="img" aria-label="Network of colourful people figures connected by lines" style="background:radial-gradient(circle at 50% 60%,#f6d36a,#e9a3c9 35%,#bfe0f5 60%,#fafafa 80%)"></div></div>
    <div class="thumb"><div class="art" role="img" aria-label="Hand holding a small red gift box" style="background:linear-gradient(135deg,#dfeef6,#b9d4e2 55%,#8a2b2b 56%,#b9d4e2 70%)"></div></div>
    <p class="caption" style="left:18px">Sed condimentum<br>ligula augue qquis</p>
    <p class="caption" style="left:190px">Sed condimentum<br>ligula augue qquis</p>
    <p class="caption" style="left:367px">Sed condimentum<br>ligula augue qquis</p>
  </section>

  <section class="news">
    <div class="news-head">What,s New</div>
    <ul class="news-list">
      <li>September 29, 2010<strong>Calvrex Media Service Day to Promote Volunteerism</strong></li>
      <li>September 24, 2010<strong>Giving the brand the right audience</strong></li>
      <li>September 16, 2010<strong>Calvrex Media&nbsp; Launches in the UK</strong></li>
    </ul>
  </section>

  <footer class="site-footer">
    <nav class="footer-links">
      <a href="#">About Us</a> | <a href="#">Contact Us</a><span class="sep">|</span><a href="#">Management Team</a><span class="sep">|</span> <a href="#">News</a><span class="sep">|</span><a href="#">Careers</a>
    </nav>
    <div class="social chirp"><span class="dot"></span>Chirpline</div>
    <div class="social wall"><span class="dot"></span>Friendwall</div>
  </footer>
</body>
</html>
```